Business Cards & Stationery for Tree Service Company
The Branch Mender
Business Cards & Stationery for Tree Service Company - Outdoors
Creative Brief
Use same font as used in my logo
It doesn't matter if you use the same font as long as it looks good I am up for creativity.
Professional
Wade Pellow
President
4817 Ransome Ave Suite 100 Des Moines, IA 50321
info@branchmenderpro.com
www.branchmenderpro.com
I would like some form of "dot" used to separate the phone and fax #'s as I think it looks cleaner and more modern. Aside from that I am looking for something cool/hip while staying clean and professional. I also need this design to be able to be edited as I need to make cards for all of my employees.
I am unaware of the proper way to make a double sided business card so I am up for the traditional way or originality whichever you prefer. I put QR Codes on a business card in the past so if you are open to ideas and you need my help for something please let me know.

```html
<!DOCTYPE html>
<html lang="en">
<head>
<meta charset="utf-8">
<title>The Branch Mender — Business Card</title>
<link rel="stylesheet" href="https://fonts.googleapis.com/css2?family=Open+Sans:wght@400;600;700;800&display=swap">
<style>
  :root {
    --bg: #e9ebec;
    --card: #ffffff;
    --blue: #1f6386;
    --blue-deep: #143f57;
    --green: #7d9b2c;
    --ink: #3c4a52;
    --muted: #6e7c84;
  }
  * { box-sizing: border-box; margin: 0; padding: 0; }
  html, body { width: 1200px; height: 864px; overflow: hidden; }
  body {
    background: var(--bg);
    font-family: "Open Sans", Arial, sans-serif;
    position: relative;
  }
  .card {
    position: absolute;
    width: 540px;
    height: 310px;
    background: var(--card);
    border-radius: 18px;
    overflow: hidden;
    box-shadow: 0 6px 22px rgba(0,0,0,0.12);
  }
  .card-front { left: 40px; top: 170px; }
  .card-back { left: 620px; top: 384px; }

  /* front */
  .front-mark {
    position: absolute; left: 0; right: 0; top: 82px;
    display: flex; flex-direction: column; align-items: center;
  }
  .mark-dot {
    width: 74px; height: 74px; border-radius: 50%;
    background: var(--blue);
  }
  .front-name {
    margin-top: 14px;
    font-size: 22px; font-weight: 800; color: var(--blue);
    letter-spacing: 0.5px;
  }
  .front-url {
    margin-top: 12px;
    font-size: 11px; font-weight: 600; color: var(--blue);
    letter-spacing: 4px;
  }

  /* back */
  .swoosh { position: absolute; inset: 0; }
  .person {
    position: absolute; right: 28px; top: 152px; text-align: right;
  }
  .person-name { font-size: 14px; font-weight: 700; color: var(--blue); }
  .person-title { font-size: 10px; color: var(--muted); margin-top: 1px; }

  .brand {
    position: absolute; left: 28px; top: 92px;
    display: flex; align-items: center; gap: 12px;
  }
  .brand .mark-dot { width: 56px; height: 56px; }
  .brand-name { font-size: 24px; font-weight: 800; color: var(--blue); line-height: 1.1; }
  .brand-tag { font-size: 10px; font-weight: 700; color: var(--green); letter-spacing: 1px; margin-top: 2px; }

  .contact {
    position: absolute; left: 28px; bottom: 22px;
    list-style: none;
  }
  .contact li {
    display: flex; align-items: center; gap: 7px;
    font-size: 9.5px; color: var(--ink); line-height: 15px;
  }
  .contact .icon {
    width: 11px; height: 11px; border-radius: 50%;
    background: var(--blue-deep); flex: none;
    display: flex; align-items: center; justify-content: center;
  }
  .contact .icon svg { width: 7px; height: 7px; }
  .contact .sep { color: var(--green); font-weight: 800; margin: 0 3px; }
</style>
</head>
<body>

<section class="card card-front">
  <div class="front-mark">
    <div class="mark-dot"></div>
    <div class="front-name">The Branch Mender</div>
    <div class="front-url">www.branchmenderpro.com</div>
  </div>
</section>

<section class="card card-back">
  <svg class="swoosh" viewBox="0 0 540 310" width="540" height="310" aria-hidden="true">
    <defs>
      <linearGradient id="bandBlue" x1="0" y1="0" x2="1" y2="1">
        <stop offset="0" stop-color="#2a7aa0"/>
        <stop offset="1" stop-color="#143f57"/>
      </linearGradient>
    </defs>
    <path d="M210 0 C300 40 450 70 540 140 L540 0 Z" fill="url(#bandBlue)"/>
    <path d="M185 0 C285 50 445 88 540 158" fill="none" stroke="#7d9b2c" stroke-width="5"/>
    <path d="M170 0 C265 54 430 100 540 172" fill="none" stroke="#7d9b2c" stroke-width="1.5" opacity="0.6"/>
  </svg>

  <div class="person">
    <div class="person-name">Wade Pellow</div>
    <div class="person-title">President</div>
  </div>

  <div class="brand">
    <div class="mark-dot"></div>
    <div>
      <div class="brand-name">The Branch Mender</div>
      <div class="brand-tag">TREE CARE SPECIALIST</div>
    </div>
  </div>

  <ul class="contact">
    <li><span class="icon"><svg viewBox="0 0 10 10"><path d="M5 0.5a3 3 0 0 0-3 3c0 2.3 3 6 3 6s3-3.7 3-6a3 3 0 0 0-3-3z" fill="#fff"/></svg></span>4817 Ransome Ave Suite 100</li>
    <li><span class="icon" style="background:transparent"></span>Des Moines, IA 50321</li>
    <li><span class="icon"><svg viewBox="0 0 10 10"><path d="M2 1l2 2-1 1.5c.8 1.4 1.6 2.2 3 3L7.5 6l2 2-1.5 1.5C4.5 9 1 5.5.5 2z" fill="#fff"/></svg></span>515.555.0142<span class="sep">•</span>515.555.0143</li>
    <li><span class="icon"><svg viewBox="0 0 10 10"><rect x="1" y="2.5" width="8" height="5" fill="none" stroke="#fff" stroke-width="1.2"/><path d="M1 2.5l4 3 4-3" fill="none" stroke="#fff" stroke-width="1"/></svg></span>info@branchmenderpro.com</li>
    <li><span class="icon"><svg viewBox="0 0 10 10"><circle cx="5" cy="5" r="3.6" fill="none" stroke="#fff" stroke-width="1"/><path d="M1.4 5h7.2M5 1.4v7.2" stroke="#fff" stroke-width="0.8"/></svg></span>www.branchmenderpro.com</li>
  </ul>
</section>

</body>
</html>
```